Business Card Design

This is a new business to be run from my home. I have attended certificate workshops run by Dr Kevin Ruddock who is a Master Trainer in Gentle Flow for Mobility.
I wish to communicate to people that Tai Chi is for everyone, no matter their age, gender or fitness levels. Tai Chi is taught both standing & seated.
The card should have a slightly Asian feel, mainly printed in black & white with perhaps a little soft pink &/or green.

Target Market(s)

people of all ages from 10 years up, poor fitness & mild disabilities.

Industry/Entity Type

Fitness

Contact Information for Business Card

Marrowdene Flowing Arts for Body, Mind & Stillness

Brenna Holcroft, Certificated Leader

ph 5281 9046

Requirements
Nice to have
• a feeling of health & peace.
Should not have
• bright colours, fancy fonts

```html
<!DOCTYPE html>
<html lang="en">
<head>
<meta charset="utf-8">
<title>Marrowdene Flowing Arts – Business Card</title>
<link rel="stylesheet" href="https://fonts.googleapis.com/css2?family=Comfortaa:wght@300;400;700&display=swap">
<style>
  :root {
    --ink: #111111;
    --ink-soft: #1f1f1f;
    --paper: #fafdf6;
    --leaf-pale: #e6f4d6;
    --leaf-mid: #cfe9b2;
    --lilac-mist: #ece3f2;
    --vine-tone: #3d4a36;
  }

  html, body {
    margin: 0;
    padding: 0;
    width: 1200px;
    height: 741px;
    overflow: hidden;
    background: #ffffff;
  }

  .card {
    position: relative;
    width: 1200px;
    height: 741px;
    overflow: hidden;
    font-family: "Comfortaa", sans-serif;
    color: var(--ink);
    background: var(--paper);
  }

  .card__backdrop {
    position: absolute;
    inset: 0;
    background:
      radial-gradient(ellipse 460px 320px at 80px 120px, var(--leaf-mid) 0%, rgba(207,233,178,0) 100%),
      radial-gradient(ellipse 420px 280px at 240px 580px, var(--leaf-mid) 0%, rgba(207,233,178,0) 100%),
      radial-gradient(ellipse 380px 240px at 720px 660px, var(--leaf-pale) 0%, rgba(230,244,214,0) 100%),
      radial-gradient(ellipse 300px 220px at 880px 240px, var(--lilac-mist) 0%, rgba(236,227,242,0) 100%),
      linear-gradient(135deg, var(--leaf-pale) 0%, var(--paper) 45%, var(--leaf-pale) 100%);
  }

  .card__ornament {
    position: absolute;
    inset: 0;
    width: 1200px;
    height: 741px;
  }

  .vine-sweep {
    fill: none;
    stroke: var(--vine-tone);
    stroke-linecap: round;
    opacity: 0.22;
  }

  .card__text {
    position: absolute;
    margin: 0;
    white-space: nowrap;
    line-height: 1;
  }

  .business-name {
    left: 74px;
    top: 92px;
    font-size: 44px;
    font-weight: 700;
  }

  .business-tagline {
    left: 74px;
    top: 156px;
    font-size: 31px;
    font-weight: 400;
    color: var(--ink-soft);
  }

  .leader-name {
    left: 74px;
    top: 274px;
    font-size: 50px;
    font-weight: 700;
  }

  .leader-title {
    left: 138px;
    top: 352px;
    font-size: 42px;
    font-weight: 300;
    color: var(--ink-soft);
  }

  .phone {
    left: 74px;
    top: 614px;
    font-size: 34px;
    font-weight: 400;
    color: var(--ink-soft);
  }
</style>
</head>
<body>
  <main class="card">
    <div class="card__backdrop" role="img" aria-label="Soft watercolour wash of pale green leaves with hints of lilac"></div>

    <svg class="card__ornament" viewBox="0 0 1200 741" role="img" aria-label="Black floral vine ornament with curling stems and blossoms, plus a small floral sprig at left">
      <defs>
        <filter id="soften" x="-20%" y="-20%" width="140%" height="140%">
          <feGaussianBlur stdDeviation="28"/>
        </filter>
      </defs>
      <g filter="url(#soften)">
        <path class="vine-sweep" stroke-width="130" d="M760 20 C880 120 1000 200 1060 320 C1110 430 1060 560 1120 700"/>
        <path class="vine-sweep" stroke-width="90" d="M680 300 C760 360 860 420 960 470"/>
        <path class="vine-sweep" stroke-width="80" d="M620 500 C720 520 820 560 900 640"/>
        <path class="vine-sweep" stroke-width="70" d="M720 80 C740 120 740 140 730 170"/>
        <path class="vine-sweep" stroke-width="70" d="M140 470 C190 460 230 460 260 470"/>
      </g>
    </svg>

    <h1 class="card__text business-name">Marrowdene Flowing Arts</h1>
    <p class="card__text business-tagline">for Body, Mind &amp; Stillness</p>

    <p class="card__text leader-name">Brenna Holcroft</p>
    <p class="card__text leader-title">Certified Leader</p>

    <p class="card__text phone">ph 5281 9046</p>
  </main>
</body>
</html>
```